ALL TEXT GRAPHICS TM May 2025 for Instagram

We are looking for a series of social media graphics for Instagram (new size: 4:5 (1080 x 1350 pixels) ratio that are ALL TEXT. We want the following quotes below on each graphic; one quote per graphic. AND, In very small letters at the bottom of each graphic, add @TovaMarshOnline
The look and feel of these graphics should be complimentary to the color palette attached below; but keep them simple. But the design is up to you; at the end of this document, I provided various samples of all text graphics that I like as examples.
Target Market(s)
women looking to lose weight
Look and feel

```html
<!DOCTYPE html>
<html lang="en">
<head>
<meta charset="utf-8">
<title>All Text Graphics – Tova Marsh</title>
<link rel="stylesheet" href="https://fonts.googleapis.com/css2?family=Barlow+Condensed:wght@500;600&family=Nunito+Sans:wght@700&display=swap">
<style>
  :root {
    --canvas: #ebebeb;
    --magenta: #d10068;
    --blush: #fb7dbd;
    --ink: #2a2a2a;
    --white: #ffffff;
  }
  * { margin: 0; padding: 0; box-sizing: border-box; }
  html, body { width: 1200px; height: 933px; overflow: hidden; background: var(--canvas); }
  .board { position: relative; width: 1200px; height: 933px; }

  .post {
    position: absolute;
    width: 288px;
    height: 360px;
    font-family: "Barlow Condensed", "Arial Narrow", sans-serif;
    text-transform: uppercase;
  }
  .post--magenta { background: var(--magenta); --line: var(--blush); --head: var(--white); --accent: var(--blush); --body: var(--white); }
  .post--white { background: var(--white); --line: var(--magenta); --head: var(--ink); --accent: var(--magenta); --body: var(--ink); }

  .col-1 { left: 88px; } .col-2 { left: 456px; } .col-3 { left: 824px; }
  .row-1 { top: 80px; } .row-2 { top: 493px; }

  .post__frame {
    position: absolute;
    left: 26px; top: 26px;
    width: 234px; height: 292px;
    border-top: 2px solid var(--line);
    border-right: 2px solid var(--line);
  }
  .post__frame::before {
    content: "";
    position: absolute;
    left: 0; top: 0;
    width: 2px; height: 54px;
    background: var(--line);
  }

  .post__headline {
    position: absolute;
    left: 25px; top: 82px;
    font-weight: 600;
    font-size: 49px;
    line-height: 42px;
    letter-spacing: 0.5px;
    color: var(--head);
  }
  .post__headline em { font-style: normal; color: var(--accent); }

  .post__body {
    position: absolute;
    left: 26px; bottom: 23px;
    font-weight: 500;
    font-size: 12.5px;
    line-height: 17px;
    color: var(--body);
  }

  .post__handle {
    position: absolute;
    left: 170px; top: 316px;
    width: 92px; height: 18px;
    background: var(--line);
    color: var(--white);
    font-family: "Nunito Sans", Arial, sans-serif;
    font-weight: 700;
    font-size: 7.5px;
    line-height: 18px;
    text-align: center;
    text-transform: none;
    letter-spacing: 0.2px;
  }
</style>
</head>
<body>
<main class="board">

  <article class="post post--magenta col-1 row-1">
    <div class="post__frame"></div>
    <h2 class="post__headline">Tired.<br>Moody.<br>Stubborn<br><em>Belly fat.</em></h2>
    <p class="post__body">Your hormones are<br>screaming for help!<br>Let’s fix that.</p>
    <span class="post__handle">@TovaMarshOnline</span>
  </article>

  <article class="post post--magenta col-2 row-1">
    <div class="post__frame"></div>
    <h2 class="post__headline">That<br>stubborn<br><em>weight?</em></h2>
    <p class="post__body">It’s not your fault.<br>Your hormones are to blame<br>and you’re not alone;<br>but there is a fix.</p>
    <span class="post__handle">@TovaMarshOnline</span>
  </article>

  <article class="post post--magenta col-3 row-1">
    <div class="post__frame"></div>
    <h2 class="post__headline">Flat<br>tummy in<br>your <em>40s?</em></h2>
    <p class="post__body">It’s still possible!<br>Comment bye belly to<br>get the 10 secrets to a<br>flatter tummy</p>
    <span class="post__handle">@TovaMarshOnline</span>
  </article>

  <article class="post post--white col-1 row-2">
    <div class="post__frame"></div>
    <h2 class="post__headline">Tired.<br>Moody.<br>Stubborn<br><em>Belly fat.</em></h2>
    <p class="post__body">Your hormones are<br>screaming for help!<br>Let’s fix that.</p>
    <span class="post__handle">@TovaMarshOnline</span>
  </article>

  <article class="post post--white col-2 row-2">
    <div class="post__frame"></div>
    <h2 class="post__headline">That<br>stubborn<br><em>weight?</em></h2>
    <p class="post__body">It’s not your fault.<br>Your hormones are to blame<br>and you’re not alone;<br>but there is a fix.</p>
    <span class="post__handle">@TovaMarshOnline</span>
  </article>

  <article class="post post--white col-3 row-2">
    <div class="post__frame"></div>
    <h2 class="post__headline">Flat<br>tummy in<br>your <em>40s?</em></h2>
    <p class="post__body">It’s still possible!<br>Comment bye belly to<br>get the 10 secrets to a<br>flatter tummy</p>
    <span class="post__handle">@TovaMarshOnline</span>
  </article>

</main>
</body>
</html>
```